Business card design for my trucking company

I would like a business card designed for my new trucking company. Please use my logo. the rest of the design is up to you. i would like my clients to say wow when they see the card. Im looking forward to seeing your designs

Target Market(s)

Industry/Entity Type

Trucking Company

Contact Information for Business Card

Marcus Tillbrook President
518-364-7120
ridgelinehaulage@examplemail.net

Font styles to use
Serif

Requirements
Must have
• my logo, name and number. we are located in Schenectady New York. the rest is up to you
Nice to have
• up to you
Should not have
• none

```html
<!DOCTYPE html>
<html lang="en">
<head>
<meta charset="utf-8">
<title>Ridgeline Haulage &amp; Freight Inc. — Business Card</title>
<link href="https://fonts.googleapis.com/css2?family=Michroma&family=Montserrat:wght@400;500&display=swap" rel="stylesheet">
<style>
  :root {
    --backdrop: #b0b0ab;
    --card-black: #1c1c1e;
    --brand-red: #e41b23;
    --white: #ffffff;
    --emboss: #3b3b3e;
  }
  * { margin: 0; padding: 0; box-sizing: border-box; }
  html, body { width: 1200px; height: 801px; overflow: hidden; }
  body { background: var(--backdrop); position: relative; font-family: "Montserrat", sans-serif; }

  .card {
    position: absolute;
    width: 520px;
    height: 297px;
    top: 252px;
    background: var(--card-black);
    overflow: hidden;
    border-bottom: 3px solid var(--brand-red);
  }
  .card--front { left: 50px; }
  .card--back { left: 630px; }

  .front-bands { position: absolute; inset: 0; }

  .holder-name {
    position: absolute; left: 28px; top: 30px;
    font-family: "Michroma", sans-serif;
    color: var(--brand-red);
    font-size: 21px; letter-spacing: 1px;
  }
  .holder-title {
    position: absolute; left: 30px; top: 62px;
    color: var(--white); font-size: 12px; letter-spacing: 0.5px;
  }
  .company-name {
    position: absolute; left: 28px; top: 112px;
    font-family: "Michroma", sans-serif;
    color: var(--white);
    font-size: 15px; line-height: 1.55; letter-spacing: 0.5px;
  }

  .address {
    position: absolute; right: 24px; top: 186px;
    color: var(--white); font-size: 11.5px; line-height: 1.5; text-align: right;
  }
  .contact-list {
    position: absolute; left: 250px; top: 232px;
    list-style: none; color: var(--white); font-size: 11px; line-height: 1.6;
  }
  .contact-list li { display: flex; align-items: center; gap: 6px; }
  .contact-list svg { width: 10px; height: 10px; flex: none; }

  .back-name {
    position: absolute; inset: 0;
    display: flex; flex-direction: column; align-items: center; justify-content: center;
    font-family: "Michroma", sans-serif;
    color: var(--emboss);
    font-size: 21px; line-height: 1.6; letter-spacing: 1px;
  }
</style>
</head>
<body>

  <section class="card card--front">
    <svg class="front-bands" viewBox="0 0 520 297" aria-hidden="true">
      <polygon points="40,297 520,90 520,297" fill="var(--brand-red)"/>
      <polygon points="18,297 520,78 520,84 30,297" fill="var(--white)"/>
    </svg>

    <h1 class="holder-name">MARCUS TILLBROOK</h1>
    <p class="holder-title">President</p>

    <p class="company-name">RIDGELINE HAULAGE<br>&amp; FREIGHT INC.</p>

    <p class="address">742 Cedar Bend Road<br>Millbrook, NY 12545</p>

    <ul class="contact-list">
      <li>
        <svg viewBox="0 0 10 10"><path d="M2 1 L4 1 L4.6 3 L3.4 3.8 Q4.5 6 6.2 6.6 L7 5.4 L9 6 L9 8 Q8.5 9 7 9 Q1 8 1 2.5 Q1 1.2 2 1 Z" fill="var(--white)"/></svg>
        518-364-7120
      </li>
      <li>
        <svg viewBox="0 0 10 10"><rect x="0.8" y="2" width="8.4" height="6" fill="none" stroke="var(--white)" stroke-width="1"/><path d="M0.8 2 L5 5.5 L9.2 2" fill="none" stroke="var(--white)" stroke-width="1"/></svg>
        ridgelinehaulage@examplemail.net
      </li>
      <li>
        <svg viewBox="0 0 10 10"><circle cx="5" cy="5" r="4.2" fill="none" stroke="var(--white)" stroke-width="1"/><path d="M0.8 5 H9.2 M5 0.8 Q2.5 5 5 9.2 M5 0.8 Q7.5 5 5 9.2" fill="none" stroke="var(--white)" stroke-width="0.8"/></svg>
        www.ridgelinehaulage.com
      </li>
    </ul>
  </section>

  <section class="card card--back">
    <p class="back-name"><span>RIDGELINE HAULAGE</span><span>&amp; FREIGHT INC.</span></p>
  </section>

</body>
</html>
```